Law Office needs stationery design and business card

I currently have been using the same letterhead for the last 8 years. Since i 'm about to adding another location, I want to revamp my letterhead and business card. I already have a logo i'm happy with. I will upload my current letterhead, fax sheet, envelope, and logos. I need a business card also. I have 2 locations, 1 phone number, 1 fax line, website, etc. If possible and fitting with the design, I would like to keep the same information listed currently on the letterhead.

**Keep in mind, I also NEED A FAX SHEET COVER. thank you

Hello, Please submit a Gray Scale or Black and White version of your designs also, since most of the time I will be printing NON color stationery. I will seldom use a color print for my letterhead, I would like to have a color version for my benefit, however i will print in grayscale majority of the time . For the Business Card, that can just be in color. When I get my business cards they will be in color.Thank youEnrique Added Sunday, September 18, 2016

```html
<!DOCTYPE html>
<html lang="en">
<head>
<meta charset="utf-8">
<title>Marvell Law Stationery</title>
<link href="https://fonts.googleapis.com/css2?family=Open+Sans:ital,wght@0,400;0,600;0,700;1,700&display=swap" rel="stylesheet">
<style>
  :root {
    --bg: #e7e7e7;
    --paper: #ffffff;
    --ink: #1e1e1e;
    --muted: #6f6f6f;
    --gold: #b8934a;
    --gold-pale: #f3e6c4;
    --gold-soft: #ead7a8;
    --rule: #c9c9c9;
  }
  * { box-sizing: border-box; margin: 0; padding: 0; }
  html, body { width: 1200px; height: 800px; overflow: hidden; }
  body { background: var(--bg); font-family: "Open Sans", Arial, sans-serif; color: var(--ink); position: relative; }

  .brand { display: flex; align-items: center; gap: 8px; }
  .brand-mark { width: 14px; height: 14px; background: var(--ink); }
  .brand-name { font-family: "Open Sans", Arial, sans-serif; font-weight: 700; color: var(--gold); letter-spacing: 0.12em; text-transform: uppercase; }

  /* Letterhead */
  .letterhead { position: absolute; left: 90px; top: 110px; width: 450px; height: 582px; background: var(--paper); box-shadow: 0 2px 8px rgba(0,0,0,.08); padding: 34px 40px; }
  .letterhead .brand-name { font-size: 15px; }
  .letterhead .attorney { font-size: 8px; font-weight: 700; font-style: italic; color: var(--gold); margin: 4px 0 0 22px; }
  .letterhead-accent { position: absolute; right: 0; top: 40px; width: 110px; height: 90px; background: linear-gradient(135deg, rgba(243,230,196,0) 0%, var(--gold-pale) 60%, var(--gold-soft) 100%); }
  .letter-body { margin-top: 56px; font-size: 8.4px; line-height: 1.5; color: var(--ink); }
  .letter-body p { margin-bottom: 12px; }
  .letter-footer { position: absolute; left: 40px; bottom: 30px; font-size: 7.5px; line-height: 1.45; color: var(--muted); }
  .letter-footer .addr { display: flex; gap: 5px; margin-bottom: 4px; }
  .letter-footer svg { width: 7px; height: 9px; flex: none; margin-top: 1px; }

  /* Card front */
  .card { position: absolute; width: 420px; height: 240px; box-shadow: 0 2px 8px rgba(0,0,0,.08); overflow: hidden; }
  .card-front { left: 650px; top: 115px; background: var(--gold-pale); display: flex; flex-direction: column; align-items: center; justify-content: center; }
  .card-front-accent { position: absolute; right: 0; top: 0; width: 170px; height: 240px; background: linear-gradient(120deg, rgba(234,215,168,0) 0%, rgba(234,215,168,.7) 70%, var(--gold-soft) 100%); }
  .card-front .brand { position: relative; }
  .card-front .brand-name { font-size: 22px; }
  .card-front .attorney { position: relative; margin-top: 16px; font-size: 11px; font-weight: 700; font-style: italic; color: var(--ink); }

  /* Card back */
  .card-back { left: 650px; top: 445px; background: var(--paper); }
  .card-back .brand { position: absolute; left: 36px; top: 104px; }
  .card-back .brand-name { font-size: 15px; }
  .card-divider { position: absolute; left: 214px; top: 36px; width: 1px; height: 150px; background: var(--rule); }
  .contact { position: absolute; left: 232px; top: 34px; font-size: 10px; line-height: 1.35; color: var(--muted); }
  .contact .attorney { font-size: 11.5px; font-weight: 700; font-style: italic; color: var(--gold); margin-bottom: 8px; }
  .contact-row { display: flex; gap: 7px; align-items: flex-start; margin-bottom: 3px; }
  .contact-row svg { width: 9px; height: 10px; flex: none; margin-top: 2px; }
  .card-band { position: absolute; left: 0; bottom: 0; width: 100%; height: 8px; display: flex; }
  .card-band .pale { width: 22%; background: var(--gold-pale); }
  .card-band .solid { flex: 1; background: var(--gold); }
</style>
</head>
<body>

<section class="letterhead">
  <div class="letterhead-accent" role="img" aria-label="Soft gold tonal accent"></div>
  <div class="brand"><span class="brand-mark"></span><span class="brand-name">Marvell Law</span></div>
  <div class="attorney">Gustavo Marvell Esq.</div>
  <div class="letter-body">
    <p>Lorem Ipsum is simply dummy text of the printing and typesetting industry. Lorem Ipsum has been the industry's standard dummy text ever since the 1500s, when an unknown printer took a galley of type and scrambled it to make a type specimen book. It has survived not only five centuries, but also the leap into electronic typesetting, remaining essentially unchanged. It was popularised in the 1960s with the release of Letraset sheets containing Lorem Ipsum passages, and more recently with desktop publishing software like Aldus PageMaker including versions of Lorem Ipsum.</p>
    <p>It is a long established fact that a reader will be distracted by the readable content of a page when looking at its layout. The point of using Lorem Ipsum is that it has a more-or-less normal distribution of letters, as opposed to using 'Content here, content here', making it look like readable English. Many desktop publishing packages and web page editors now use Lorem Ipsum as their default model text, and a search for 'lorem ipsum' will uncover many web sites still in their infancy. Various versions have evolved over the years, sometimes by accident, sometimes on purpose (injected humour and the like).</p>
    <p>Contrary to popular belief, Lorem Ipsum is not simply random text. It has roots in a piece of classical Latin literature from 45 BC, making it over 2000 years old. A Latin professor in Virginia looked up one of the more obscure Latin words, consectetur, from a Lorem Ipsum passage, and going through the cites of the word in classical literature, discovered the undoubtable source.</p>
  </div>
  <div class="letter-footer">
    <div class="addr"><svg viewBox="0 0 10 13"><path d="M5 0a4.5 4.5 0 0 0-4.5 4.5C.5 8 5 13 5 13s4.5-5 4.5-8.5A4.5 4.5 0 0 0 5 0zm0 6.3a1.8 1.8 0 1 1 0-3.6 1.8 1.8 0 0 1 0 3.6z" fill="#b8934a"/></svg><span>48 North Grove St., Suite 210<br>Alden, PA 19170</span></div>
    <div class="addr"><svg viewBox="0 0 10 13"><path d="M5 0a4.5 4.5 0 0 0-4.5 4.5C.5 8 5 13 5 13s4.5-5 4.5-8.5A4.5 4.5 0 0 0 5 0zm0 6.3a1.8 1.8 0 1 1 0-3.6 1.8 1.8 0 0 1 0 3.6z" fill="#b8934a"/></svg><span>917 Carlow St, Brayton,<br>PA 19422</span></div>
  </div>
</section>

<section class="card card-front">
  <div class="card-front-accent" role="img" aria-label="Soft gold tonal accent"></div>
  <div class="brand"><span class="brand-mark"></span><span class="brand-name">Marvell Law</span></div>
  <div class="attorney">Gustavo Marvell Esq.</div>
</section>

<section class="card card-back">
  <div class="brand"><span class="brand-mark"></span><span class="brand-name">Marvell Law</span></div>
  <div class="card-divider"></div>
  <div class="contact">
    <div class="attorney">Gustavo Marvell Esq.</div>
    <div class="contact-row"><svg viewBox="0 0 10 13"><path d="M5 0a4.5 4.5 0 0 0-4.5 4.5C.5 8 5 13 5 13s4.5-5 4.5-8.5A4.5 4.5 0 0 0 5 0zm0 6.3a1.8 1.8 0 1 1 0-3.6 1.8 1.8 0 0 1 0 3.6z" fill="#b8934a"/></svg><span>48 North Grove St., Suite 210,<br>Alden, PA 19170</span></div>
    <div class="contact-row"><svg viewBox="0 0 10 13"><path d="M5 0a4.5 4.5 0 0 0-4.5 4.5C.5 8 5 13 5 13s4.5-5 4.5-8.5A4.5 4.5 0 0 0 5 0zm0 6.3a1.8 1.8 0 1 1 0-3.6 1.8 1.8 0 0 1 0 3.6z" fill="#b8934a"/></svg><span>917 Carlow St, Brayton,<br>PA 19422</span></div>
    <div class="contact-row"><svg viewBox="0 0 12 12"><path d="M2.5 1 4.5 1 5.3 3.5 4 4.6a7 7 0 0 0 3.4 3.4L8.5 6.7 11 7.5v2c0 .8-.7 1.5-1.5 1.5A9 9 0 0 1 1 2.5C1 1.7 1.7 1 2.5 1z" fill="none" stroke="#b8934a" stroke-width="1.1"/></svg><span>610.555.0172</span></div>
    <div class="contact-row"><svg viewBox="0 0 12 12"><rect x="1" y="4" width="10" height="6" rx="1" fill="none" stroke="#b8934a" stroke-width="1.1"/><rect x="3" y="1.5" width="6" height="3" fill="none" stroke="#b8934a" stroke-width="1.1"/></svg><span>484.555.0193</span></div>
    <div class="contact-row"><svg viewBox="0 0 12 12"><circle cx="6" cy="6" r="5" fill="none" stroke="#b8934a" stroke-width="1.1"/><path d="M1 6h10M6 1c2.5 3 2.5 7 0 10M6 1c-2.5 3-2.5 7 0 10" fill="none" stroke="#b8934a" stroke-width=".9"/></svg><span>www.MarvellLaw.com</span></div>
    <div class="contact-row"><svg viewBox="0 0 12 12"><circle cx="6" cy="6" r="5" fill="none" stroke="#b8934a" stroke-width="1.1"/></svg><span>MarvellLaw</span></div>
  </div>
  <div class="card-band"><span class="pale"></span><span class="solid"></span></div>
</section>

</body>
</html>
```